Australian Software Consultancy needs new Business Card Design

Design Business Card based on existing design artefacts (attached). We are open to all designs. As its a 2 sided design and we thought it might be quite striking to have one side with a black background and te other side with a white background.

Target Market(s)

Financial Services mainly.

Industry/Entity Type

Business

Contact Information for Business Card

Requirements
Must have
• Funky design using our existing assets

```html
<!DOCTYPE html>
<html lang="en">
<head>
<meta charset="utf-8">
<title>Business Card – Front and Back</title>
<link rel="stylesheet" href="https://fonts.googleapis.com/css2?family=Poppins:wght@400;600&display=swap">
<style>
  :root {
    --backdrop: #c2c2c2;
    --card-top: #2f2f30;
    --card-bottom: #232324;
    --text-light: #f4f4f4;
    --text-muted: #cfcfcf;
    --accent-red: #e0262b;
  }
  * { box-sizing: border-box; margin: 0; padding: 0; }
  html, body {
    width: 1200px;
    height: 1000px;
    overflow: hidden;
    background: var(--backdrop);
    font-family: "Poppins", sans-serif;
  }
  .sheet {
    width: 1200px;
    height: 1000px;
    display: flex;
    flex-direction: column;
    align-items: center;
    justify-content: center;
    gap: 50px;
  }
  .card {
    width: 700px;
    height: 400px;
    background: linear-gradient(160deg, var(--card-top), var(--card-bottom));
    box-shadow: 0 6px 18px rgba(0, 0, 0, 0.35);
    display: flex;
    align-items: center;
    justify-content: center;
  }
  .contact-block {
    display: flex;
    align-items: center;
    gap: 18px;
    margin-left: -20px;
  }
  .identity {
    text-align: right;
  }
  .identity-name {
    color: var(--text-light);
    font-weight: 600;
    font-size: 27px;
    letter-spacing: 1px;
    line-height: 1.1;
  }
  .identity-role {
    color: var(--accent-red);
    font-weight: 400;
    font-size: 15px;
    letter-spacing: 1.5px;
    margin-top: 2px;
  }
  .divider {
    width: 5px;
    height: 58px;
    background: var(--accent-red);
  }
  .contact-list {
    list-style: none;
    display: flex;
    flex-direction: column;
    gap: 8px;
  }
  .contact-item {
    display: flex;
    align-items: center;
    gap: 12px;
    color: var(--text-light);
    font-size: 16px;
    letter-spacing: 0.6px;
  }
  .contact-icon { width: 16px; height: 16px; flex: none; }
  .brand-name {
    color: var(--text-muted);
    font-weight: 600;
    font-size: 54px;
    letter-spacing: 2px;
  }
</style>
</head>
<body>
<main class="sheet">
  <section class="card card-front" aria-label="Card front">
    <div class="contact-block">
      <div class="identity">
        <p class="identity-name">DANIEL REYES</p>
        <p class="identity-role">FOUNDER</p>
      </div>
      <span class="divider"></span>
      <ul class="contact-list">
        <li class="contact-item">
          <svg class="contact-icon" viewBox="0 0 16 16" aria-hidden="true">
            <circle cx="8" cy="8" r="8" fill="var(--accent-red)"/>
            <path d="M5.2 4.2l1.4-.4.9 2-1 .8a5 5 0 0 0 2.9 2.9l.8-1 2 .9-.4 1.4c-.2.5-.7.8-1.2.7A7 7 0 0 1 4.5 5.4c-.1-.5.2-1 .7-1.2z" fill="var(--card-bottom)"/>
          </svg>
          000 000 0000
        </li>
        <li class="contact-item">
          <svg class="contact-icon" viewBox="0 0 16 16" aria-hidden="true">
            <circle cx="8" cy="8" r="8" fill="var(--accent-red)"/>
            <rect x="4" y="5" width="8" height="6" rx="0.8" fill="var(--card-bottom)"/>
            <path d="M4.4 5.6L8 8.4l3.6-2.8" stroke="var(--accent-red)" stroke-width="1" fill="none"/>
          </svg>
          info@danielreyes.com
        </li>
      </ul>
    </div>
  </section>

  <section class="card card-back" aria-label="Card back">
    <p class="brand-name">NORTHFOLD</p>
  </section>
</main>
</body>
</html>
```